Brand new letterhead, business card, email signature etc.

We are a financial company in London, UK. Our website is www.quorvane.com. We're wanting a complete remodel of the company colours, letter head, business cards, email signatures, etc. Looking to keep the same font for the company name. I have upload a colour palette that we want to work with. We're looking for company letterhead for outgoing letters/ correspondence, letterhead for internal documentation, email signatures, e-letters. etc. Ultimately we will redesign the entire website also. It is important that our clients get a strong, secure, warm, trustworthy, solid feeling and first impression.
Updates

Designs look the same

Target Market(s)

Institutional investors, (ultra) high net worth individuals

Industry/Entity Type

Finance, Invesments banking.

Font styles to use
Other font styles liked:
• Current font is "Champagne & Limousines"

Requirements
Must have
• Must use the colours provided on the PDF uploaded to the portal. The purple = main colour. The red = accent colour.
Nice to have
• Nice to use same font as now for the company name "Marlowin". Font is "Champagne & Limousines". Nice to have some reference to the old logo flower, but only subtle.
Should not have
• Do not use the colour red from our website. Use the colours provided on the colour palette PDF that I uploaded in the portal.

```html
<!DOCTYPE html>
<html lang="en">
<head>
<meta charset="utf-8">
<title>Marlowin Stationery</title>
<link rel="stylesheet" href="https://fonts.googleapis.com/css2?family=Jost:wght@300;400&family=Montserrat:wght@400&display=swap">
<style>
  :root{
    --backdrop:#e6e6e6;
    --paper:#ffffff;
    --plum:#2e0419;
    --vermilion:#e23a1d;
    --ink:#1f1a1c;
    --muted:#6b6466;
    --mark-line:#3a3436;
    --decor-a:#f4f2f3;
    --decor-b:#fbf6f7;
  }
  *{box-sizing:border-box;margin:0;padding:0}
  html,body{width:1129px;height:1200px;overflow:hidden;background:var(--backdrop)}
  body{position:relative;font-family:"Montserrat",sans-serif;color:var(--ink)}

  .sheet{position:absolute;background:var(--paper);overflow:hidden;box-shadow:0 4px 14px rgba(0,0,0,.18)}
  .brand-bar{position:absolute;left:0;right:0;bottom:0;height:7px;display:flex}
  .brand-bar .plum{background:var(--plum)}
  .brand-bar .accent{background:var(--vermilion);flex:1}

  .wordmark{position:absolute;display:flex;align-items:center;white-space:nowrap}
  .wordmark .tile{border:1px solid var(--mark-line);flex:none}
  .wordmark .name{font-family:"Jost",sans-serif;font-weight:300;text-transform:uppercase;color:var(--ink);line-height:1}

  .decor{position:absolute;background:radial-gradient(ellipse at 55% 55%,var(--decor-b),var(--decor-a) 60%,var(--paper) 100%)}

  .contacts{position:absolute;list-style:none;font-size:11px;color:var(--ink);white-space:nowrap}
  .contacts li{display:flex;align-items:center;gap:6px;height:15.5px}
  .contacts svg{width:9px;height:9px;flex:none}

  /* email signature */
  .signature{left:399px;top:73px;width:572px;height:227px}
  .signature .brand-bar .plum{width:284px}
  .signature .decor{left:0;top:0;width:185px;height:220px}
  .signature .wordmark{left:227px;top:37px}
  .signature .tile{width:70px;height:70px}
  .signature .name{font-size:36px;letter-spacing:4px;margin-left:17px}
  .signature .contacts{left:227px;top:133px}

  /* letterhead */
  .letterhead{left:340px;top:351px;width:543px;height:765px}
  .letterhead .brand-bar .plum{width:273px}
  .letterhead .decor{left:0;top:242px;width:514px;height:516px}
  .letterhead .wordmark{left:53px;top:44px}
  .letterhead .tile{width:48px;height:48px}
  .letterhead .name{font-size:24px;letter-spacing:3.5px;margin-left:12px}
  .letterhead .contacts{left:370px;top:31px}

  /* business card */
  .card{position:absolute;border-radius:9px;overflow:hidden;box-shadow:0 3px 10px rgba(0,0,0,.18)}
  .card-front{left:65px;top:609px;width:230px;height:131px;background:var(--paper)}
  .card-front .wordmark{left:42px;top:22px}
  .card-front .tile{width:36px;height:36px}
  .card-front .name{font-size:17px;letter-spacing:2.5px;margin-left:9px}
  .card-front .person{position:absolute;right:116px;top:71px;text-align:right;white-space:nowrap}
  .person .full-name{font-family:"Jost",sans-serif;font-size:9px;color:var(--plum);text-transform:uppercase;letter-spacing:-.2px}
  .person .role{font-family:"Jost",sans-serif;font-size:5px;color:var(--muted);text-transform:uppercase;margin-top:2px}
  .card-front .divider{position:absolute;left:121px;top:70px;width:1px;height:22px;background:#c9c3c5}
  .card-front .contacts{left:127px;top:67px;font-size:5px;color:var(--muted)}
  .card-front .contacts li{height:8.5px;gap:3px}
  .card-front .contacts svg{width:5px;height:5px}
  .address-band{position:absolute;left:0;right:0;top:104px;height:11px;background:var(--plum);color:#fff;font-size:5.5px;display:flex;align-items:center;justify-content:center;gap:3px;white-space:nowrap}
  .address-band svg{width:5px;height:6px}

  .card-back{left:68px;top:750px;width:230px;height:131px;background:var(--plum)}
  .card-back .wordmark{left:34px;top:45px}
  .card-back .tile{width:40px;height:40px;border-color:#e9dfe3}
  .card-back .name{font-size:19px;letter-spacing:3px;margin-left:10px;color:#fff}
</style>
</head>
<body>

<section class="sheet signature">
  <div class="decor" role="img" aria-label="Faint line-drawn floral decoration"></div>
  <div class="wordmark"><span class="tile"></span><span class="name">Marlowin</span></div>
  <ul class="contacts">
    <li><svg viewBox="0 0 10 10"><path d="M2 1l2 2-1 1.2c.6 1.3 1.5 2.2 2.8 2.8L7 6l2 2-1.3 1.3C4.5 9 1 5.5.7 2.3z" fill="var(--ink)"/></svg>020-7946 0381</li>
    <li><svg viewBox="0 0 10 10"><rect x="0.5" y="2" width="9" height="6" fill="var(--ink)"/><path d="M.5 2l4.5 3.5L9.5 2" stroke="#fff" stroke-width=".8" fill="none"/></svg>info@quorvane.com</li>
    <li><svg viewBox="0 0 10 10" fill="none" stroke="var(--ink)" stroke-width=".9"><circle cx="5" cy="5" r="4.2"/><ellipse cx="5" cy="5" rx="1.8" ry="4.2"/><path d="M.8 5h8.4"/></svg>www.quorvane.com</li>
  </ul>
  <div class="brand-bar"><span class="plum"></span><span class="accent"></span></div>
</section>

<section class="sheet letterhead">
  <div class="wordmark"><span class="tile"></span><span class="name">Marlowin</span></div>
  <ul class="contacts">
    <li><svg viewBox="0 0 10 10"><path d="M2 1l2 2-1 1.2c.6 1.3 1.5 2.2 2.8 2.8L7 6l2 2-1.3 1.3C4.5 9 1 5.5.7 2.3z" fill="var(--ink)"/></svg>020-7946 0381</li>
    <li><svg viewBox="0 0 10 10"><rect x="0.5" y="2" width="9" height="6" fill="var(--ink)"/><path d="M.5 2l4.5 3.5L9.5 2" stroke="#fff" stroke-width=".8" fill="none"/></svg>info@quorvane.com</li>
    <li><svg viewBox="0 0 10 10" fill="none" stroke="var(--ink)" stroke-width=".9"><circle cx="5" cy="5" r="4.2"/><ellipse cx="5" cy="5" rx="1.8" ry="4.2"/><path d="M.8 5h8.4"/></svg>www.quorvane.com</li>
  </ul>
  <div class="decor" role="img" aria-label="Large faint line-drawn floral decoration"></div>
  <div class="brand-bar"><span class="plum"></span><span class="accent"></span></div>
</section>

<section class="card card-front">
  <div class="wordmark"><span class="tile"></span><span class="name">Marlowin</span></div>
  <div class="person">
    <p class="full-name">Edmund Harrow</p>
    <p class="role">Managing Director</p>
  </div>
  <span class="divider"></span>
  <ul class="contacts">
    <li><svg viewBox="0 0 10 10"><path d="M2 1l2 2-1 1.2c.6 1.3 1.5 2.2 2.8 2.8L7 6l2 2-1.3 1.3C4.5 9 1 5.5.7 2.3z" fill="var(--vermilion)"/></svg>020-7946 0381</li>
    <li><svg viewBox="0 0 10 10"><rect x="0.5" y="2" width="9" height="6" fill="var(--vermilion)"/><path d="M.5 2l4.5 3.5L9.5 2" stroke="#fff" stroke-width=".8" fill="none"/></svg>info@quorvane.com</li>
    <li><svg viewBox="0 0 10 10"><circle cx="5" cy="5" r="4.5" fill="var(--vermilion)"/></svg>www.quorvane.com</li>
  </ul>
  <div class="address-band">
    <svg viewBox="0 0 10 12"><path d="M5 0a4 4 0 00-4 4c0 3 4 8 4 8s4-5 4-8a4 4 0 00-4-4z" fill="var(--vermilion)"/><circle cx="5" cy="4" r="1.5" fill="var(--plum)"/></svg>
    421, Address line goes here 45452, Country name
  </div>
</section>

<section class="card card-back">
  <div class="wordmark"><span class="tile"></span><span class="name">Marlowin</span></div>
</section>

</body>
</html>
```